Plumbing Product Supply Company Needs Front & Back Cover Design For Instruction Manuals

We need a front and back over design for our instruction manuals that we need to give to clients.

There will also be a picture of the product on the front cover so please use the supplied image as dummy.

it needs to incorporate our logo and branding colours.

We are the industry leader so it needs to be up-market, professional and stand out from the crowd.

Target Market(s)

Plumbing Companies

Industry/Entity Type

Plumbing

Font styles to use
Sans Serif

Colors
abd036
ffffff
000000
eaeaea
cbcbcb

Requirements
Must have
• Front & Back Cover as it will become a booklet.
• The logo is to be on the black background.
Nice to have
• Professional, modern, sleek.
Should not have
• Other colours that what is on the guidelines.

```html
<!DOCTYPE html>
<html lang="en">
<head>
<meta charset="utf-8">
<title>Keystone Relining Supplies – Manual Covers</title>
<link href="https://fonts.googleapis.com/css2?family=Montserrat:wght@300;400;600;800&family=Raleway:wght@300;400&display=swap" rel="stylesheet">
<style>
  :root {
    --brand-green: #abd036;
    --white: #ffffff;
    --black: #000000;
    --light-grey: #eaeaea;
    --mid-grey: #cbcbcb;
  }
  * { box-sizing: border-box; margin: 0; padding: 0; }
  html, body { width: 1200px; height: 900px; overflow: hidden; }
  body {
    background: var(--light-grey);
    font-family: "Montserrat", sans-serif;
    position: relative;
  }
  .spread {
    position: absolute;
    left: 185px; top: 165px;
    display: flex; gap: 20px;
  }
  .cover {
    position: relative;
    width: 405px; height: 570px;
    overflow: hidden;
  }

  /* Back cover */
  .cover--back { background: var(--black); }
  .back-brand {
    position: absolute; left: 0; right: 0; top: 395px;
    text-align: center;
    font-weight: 800; font-size: 84px; letter-spacing: 2px;
    color: var(--brand-green); line-height: 1;
  }
  .contact-row {
    position: absolute; left: 0; right: 0; top: 498px;
    display: flex; justify-content: center; gap: 14px;
    font-size: 7.5px; color: var(--mid-grey);
  }
  .contact-item { display: flex; align-items: center; gap: 5px; }
  .contact-icon {
    width: 13px; height: 13px; border-radius: 50%;
    background: var(--brand-green);
    display: flex; align-items: center; justify-content: center;
  }

  /* Front cover */
  .cover--front { background: var(--white); }
  .front-shapes { position: absolute; inset: 0; }
  .front-brand {
    position: absolute; left: 85px; width: 240px; top: 104px;
    text-align: center;
  }
  .front-brand__name {
    font-weight: 800; font-size: 84px; letter-spacing: 2px;
    color: var(--brand-green); line-height: 1;
  }
  .front-brand__tag {
    display: flex; align-items: center; gap: 8px;
    margin-top: 6px;
    font-family: "Raleway", sans-serif; font-weight: 400;
    font-size: 13px; letter-spacing: 5px; color: var(--white);
  }
  .front-brand__tag::before, .front-brand__tag::after {
    content: ""; flex: 1; height: 1px; background: var(--mid-grey);
  }
  .front-brand__line {
    font-family: "Raleway", sans-serif; font-weight: 300;
    font-size: 23px; color: var(--white); margin-top: 2px; white-space: nowrap;
  }
  .product-photo {
    position: absolute; left: 52px; top: 255px;
    width: 300px; height: 230px;
    background: radial-gradient(ellipse at center, #d8d8d8 0%, #bdbdbd 55%, rgba(234,234,234,0) 80%);
  }
  .front-title {
    position: absolute; left: 60px; right: 0; top: 506px;
    text-align: center;
    font-size: 17px; color: var(--black); font-weight: 300;
  }
  .front-title strong { font-weight: 600; }
  .front-title__rule {
    display: block; width: 60px; height: 4px;
    background: var(--brand-green); margin: 6px auto 0;
  }
</style>
</head>
<body>
  <main class="spread">
    <section class="cover cover--back" aria-label="Back cover">
      <div class="back-brand">KTR</div>
      <div class="contact-row">
        <span class="contact-item">
          <span class="contact-icon"><svg width="7" height="7" viewBox="0 0 10 10"><rect x="1.5" y="2" width="7" height="7" fill="#000"/><rect x="3" y="4" width="1.5" height="1.5" fill="#abd036"/><rect x="5.5" y="4" width="1.5" height="1.5" fill="#abd036"/></svg></span>
          Address will come here
        </span>
        <span class="contact-item">
          <span class="contact-icon"><svg width="7" height="7" viewBox="0 0 10 10"><path d="M2 1 L4 1 L4.8 3.2 L3.6 4.2 Q4.6 6 6 6.6 L7 5.4 L9 6.2 L9 8.2 Q4 8.6 1.6 3 Z" fill="#000"/></svg></span>
          0000 000 00
        </span>
        <span class="contact-item">
          <span class="contact-icon"><svg width="7" height="7" viewBox="0 0 10 10"><circle cx="5" cy="5" r="4" fill="none" stroke="#000" stroke-width="1"/><ellipse cx="5" cy="5" rx="1.8" ry="4" fill="none" stroke="#000" stroke-width="0.8"/><line x1="1" y1="5" x2="9" y2="5" stroke="#000" stroke-width="0.8"/></svg></span>
          www.ktr.com
        </span>
      </div>
    </section>

    <section class="cover cover--front" aria-label="Front cover">
      <svg class="front-shapes" width="405" height="570" viewBox="0 0 405 570">
        <path d="M0 150 Q150 45 405 42 L405 255 Q250 230 120 330 Q55 395 40 570 L0 570 Z" fill="var(--black)"/>
        <path d="M170 45 Q270 8 405 5 L405 30 Q280 22 170 45 Z" fill="var(--brand-green)"/>
        <path d="M120 330 Q70 380 52 440 Q45 500 40 570 L56 570 Q58 490 72 440 Q90 380 135 320 Z" fill="var(--brand-green)"/>
      </svg>
      <div class="front-brand">
        <div class="front-brand__name">KTR</div>
        <div class="front-brand__tag">KEYSTONE</div>
        <div class="front-brand__line">RELINING SUPPLIES</div>
      </div>
      <div class="product-photo" role="img" aria-label="Product kit photo: relining resin containers, tool case, liner rolls, air hose and push rods"></div>
      <div class="front-title"><strong>LOREM IPSUM</strong> LOREM IPSUM<span class="front-title__rule"></span></div>
    </section>
  </main>
</body>
</html>
```